Lunaryth needs a elegant mystical business card design

The theme of Lunaryth is centered on Kemetic/Ancient Egyptian Spirituality. My business sells handmade scented candles, mystic oils, body sprays, tarot readings and more. I would like my business card to reflect an elegant and mystical look. Hieroglyphs around the borders would be a cool idea. Also, the main colors I am working with is Black and Gold= colors of royalty. Black background. The business card will be double sided. The back will have the logo, and the front will have the basic information (ie name, title, business, phone, email, website, etc..)

Target Market(s)

The target market are people into metaphysics, holistic healing, ancient Egyptian culture, aromatherapy, occult science, and the esoteric.

Industry/Entity Type

Business

Contact Information for Business Card

Name: Marisol T. Pike
Title: Owner
Business: LUNARYTH
Phone: 555.210.4473
Website: www.Lunaryth.example
Facebook, Instagram, and twitter icons

Font styles to use
Serif
Decorative

Requirements
Must have
• My logo, and website.
Nice to have
• Ancient Egyptian hieroglyphs, Elegant designs around the border, or encircling the logo.

```html
<!DOCTYPE html>
<html lang="en">
<head>
<meta charset="utf-8">
<title>Lunaryth Business Card</title>
<link href="https://fonts.googleapis.com/css2?family=Source+Sans+3:wght@400;600;700&display=swap" rel="stylesheet">
<style>
  :root {
    --backdrop: #e8e4df;
    --gold-dark: #8a6d3e;
    --gold-mid: #c9ae7c;
    --gold-light: #d6bf94;
    --gold-text: #c8a565;
    --ink: #111111;
    --card-black: #000000;
  }
  html, body {
    margin: 0;
    padding: 0;
    width: 1200px;
    height: 900px;
    overflow: hidden;
    background: var(--backdrop);
    font-family: "Source Sans 3", Arial, sans-serif;
  }
  .canvas {
    position: relative;
    width: 1200px;
    height: 900px;
  }
  .card {
    position: absolute;
    box-shadow: 0 6px 18px rgba(0,0,0,0.18);
  }
  .card-front {
    left: 237px;
    top: 62px;
    width: 556px;
    height: 342px;
    background: linear-gradient(180deg, var(--gold-dark) 0%, var(--gold-mid) 35%, var(--gold-light) 55%, var(--gold-mid) 78%, var(--gold-dark) 100%);
    color: var(--ink);
  }
  .card-back {
    left: 457px;
    top: 518px;
    width: 560px;
    height: 343px;
    background: var(--card-black);
  }
  .brand {
    position: absolute;
    transform: translate(-50%, -50%);
    font-weight: 600;
    letter-spacing: 4px;
    white-space: nowrap;
  }
  .card-front .brand {
    left: 371px;
    top: 72px;
    font-size: 26px;
    color: var(--ink);
  }
  .card-back .brand {
    left: 280px;
    top: 160px;
    font-size: 28px;
    color: var(--gold-text);
  }
  .holder-name {
    position: absolute;
    left: 47px;
    top: 156px;
    margin: 0;
    font-size: 21px;
    font-weight: 700;
  }
  .holder-title {
    position: absolute;
    left: 47px;
    top: 181px;
    margin: 0;
    font-size: 14px;
  }
  .contact-list {
    position: absolute;
    left: 47px;
    top: 218px;
    margin: 0;
    padding: 0;
    list-style: none;
    font-size: 15px;
  }
  .contact-list li {
    display: flex;
    align-items: center;
    gap: 8px;
    height: 23px;
  }
  .contact-list svg { width: 12px; height: 12px; }
  .social-row {
    position: absolute;
    left: 47px;
    top: 290px;
    display: flex;
    gap: 13px;
  }
  .social-slot {
    width: 18px;
    height: 18px;
    background: var(--ink);
    border-radius: 2px;
  }
</style>
</head>
<body>
<main class="canvas">
  <section class="card card-front" aria-label="Card front">
    <div class="brand">LUNARYTH</div>
    <h1 class="holder-name">Marisol T. Pike</h1>
    <p class="holder-title">Owner</p>
    <ul class="contact-list">
      <li>
        <svg viewBox="0 0 24 24" aria-hidden="true"><path fill="currentColor" d="M6.6 10.8a15.1 15.1 0 0 0 6.6 6.6l2.2-2.2c.3-.3.7-.4 1-.2 1.1.4 2.3.6 3.6.6.6 0 1 .4 1 1V20c0 .6-.4 1-1 1A17 17 0 0 1 3 4c0-.6.4-1 1-1h3.5c.6 0 1 .4 1 1 0 1.3.2 2.5.6 3.6.1.3 0 .7-.2 1z"/></svg>
        <span>555.210.4473</span>
      </li>
      <li>
        <svg viewBox="0 0 24 24" aria-hidden="true"><circle cx="12" cy="12" r="10" fill="currentColor"/><path d="M2 12h20M12 2c3 3 3 17 0 20M12 2c-3 3-3 17 0 20" stroke="#c9ae7c" stroke-width="1.5" fill="none"/></svg>
        <span>www.Lunaryth.example</span>
      </li>
    </ul>
    <div class="social-row" aria-label="Social profiles">
      <span class="social-slot"></span>
      <span class="social-slot"></span>
      <span class="social-slot"></span>
    </div>
  </section>

  <section class="card card-back" aria-label="Card back">
    <div class="brand">LUNARYTH</div>
  </section>
</main>
</body>
</html>
```